Blind Rivet Product catalogue

Need a design in wordpress with a productcatalogue where i present all products. This is a B2B business. The products is Blindrivets and Blindrivet nuts and accessories to this. I only want the basic information and also technical specification.

This is a subcompany to my existing company k7.m9.se but specializing in a subcategory

Target Market(s)

Businesses using blind rivet technology.

Industry/Entity Type

Industrial

Coding

Coded - Design and coding required

Number of Pages Required

5+ page

Font styles to use
Sans Serif

Requirements
Must have
• Three different categories for the products; Blind Rivets - Blind Rivet Nut - Riveting Tools
Nice to have
• Possible to ad login for more information of the different sizes

```html
<!DOCTYPE html>
<html lang="en">
<head>
<meta charset="utf-8">
<title>K7M9 — Blind Rivet Nuts &amp; Accessories</title>
<link rel="stylesheet" href="https://fonts.googleapis.com/css2?family=Exo+2:wght@500;600;700&family=Lato:wght@400;700&display=swap">
<style>
:root{
  --black:#0b0b0b;
  --dark:#262626;
  --panel:#3a3a3a;
  --red:#c4161c;
  --red-dark:#5a0a0c;
  --white:#ffffff;
  --text:#333333;
  --muted:#666666;
  --light:#f2f2f2;
  --head:"Exo 2",sans-serif;
  --body:"Lato",sans-serif;
}
*{box-sizing:border-box;margin:0;padding:0}
html,body{width:1200px;height:3432px;overflow:hidden}
body{position:relative;background:var(--white);font-family:var(--body);color:var(--text)}
.abs{position:absolute}
.heading-rule{position:absolute;height:3px;background:currentColor}

/* header */
.site-header{left:0;top:0;width:1200px;height:104px;background:var(--black)}
.brand{left:130px;top:36px;display:flex;align-items:center;gap:8px;color:var(--white);font-family:var(--head);font-weight:700;font-size:26px;letter-spacing:1px}
.brand-mark{width:14px;height:14px;background:var(--red)}
.main-nav{left:255px;top:40px;display:flex;font-family:var(--head);font-weight:600;font-size:14px;color:var(--white)}
.main-nav span{margin-right:35px}
.main-nav .active{color:var(--red)}
.login-btn{left:973px;top:31px;width:92px;height:35px;border:2px solid var(--red);color:var(--red);font-family:var(--head);font-weight:600;font-size:14px;display:flex;align-items:center;justify-content:center}
.cart{left:1088px;top:38px}
.cart-count{left:1102px;top:34px;width:19px;height:19px;border-radius:50%;background:var(--white);color:var(--black);font-size:12px;font-weight:700;display:flex;align-items:center;justify-content:center}

/* hero */
.hero-visual{left:0;top:104px;width:1200px;height:603px;background:linear-gradient(115deg,#4a4a4a 0%,#2c2c2c 40%,#8e1216 55%,#c41a20 100%)}
.hero-kicker{left:127px;top:252px;color:var(--red);font-family:var(--head);font-weight:700;font-size:27px}
.hero-title{left:127px;top:292px;color:var(--white);font-family:var(--head);font-weight:700;font-size:45px;line-height:44px}
.hero-title .dim{color:#c8c8c8}
.hero-copy{left:128px;top:396px;color:#e6e6e6;font-size:16px;line-height:21px}
.btn-outline{display:flex;align-items:center;justify-content:center;font-family:var(--body);font-weight:700;font-size:15px;border:2px solid var(--white);color:var(--white)}
.hero-btn{left:128px;top:459px;width:180px;height:47px}
.hero-arrow{top:356px}

/* categories */
.cat-card{display:flex;flex-direction:column;align-items:center;text-align:center;background:linear-gradient(#ffffff,#ededed);border:1px solid #dcdcdc;box-shadow:0 2px 6px rgba(0,0,0,.12)}
.cat-card h3{font-family:var(--head);font-weight:600;font-size:22px;color:#222;margin-top:14px}
.cat-card p{font-size:11px;line-height:17px;color:#555;margin-top:6px;width:230px}
.cat-img{width:180px;height:125px;background:radial-gradient(#d8d8d8,#f2f2f2 70%)}
.cat-card.featured{background:linear-gradient(#b9161b,#4a0709);border:none;box-shadow:0 4px 14px rgba(0,0,0,.35);z-index:2}
.cat-card.featured h3,.cat-card.featured p{color:var(--white)}
.cat-card.featured .cat-img{background:radial-gradient(#e0e0e0,#b3161b 70%)}
.cat-down{width:38px;height:38px;border:2px solid var(--white);border-radius:50%;margin-top:14px;display:flex;align-items:center;justify-content:center}

/* about */
.about-band{left:0;top:1181px}
.about-img{left:160px;top:1272px;width:373px;height:280px;background:radial-gradient(#9a9a9a,#3a3a3a 70%)}
.about-title{left:605px;top:1290px;color:var(--white);font-family:var(--head);font-weight:700;font-size:36px}
.about-copy{left:604px;top:1375px;width:470px;color:#f0f0f0;font-size:15.5px;line-height:23px}
.about-copy p+p{margin-top:9px}
.about-btn{left:605px;top:1549px;width:166px;height:46px}

/* section heading */
.sec-title{left:0;width:1200px;text-align:center;font-family:var(--head);font-weight:700;font-size:31px;color:#111}

/* latest products */
.product{width:250px;text-align:center}
.product-img{width:110px;height:110px;margin:0 auto;background:radial-gradient(#9a9a9a,#eeeeee 70%)}
.product h4{font-family:var(--head);font-weight:600;font-size:20px;color:#222;margin-top:48px}
.product p{font-size:12px;line-height:15px;color:#444;margin-top:8px}
.btn-red{display:inline-flex;align-items:center;justify-content:center;width:130px;height:37px;border:2px solid var(--red);color:var(--red);font-weight:700;font-size:13px;margin-top:22px}
.divider{width:1px;background:#d0d0d0;top:1870px;height:282px}

/* other products */
.other-band{left:0;top:2208px}
.other-card{width:212px}
.other-img{height:144px;background:linear-gradient(135deg,#6a6a6a,#2f2f2f)}
.other-info{width:194px;margin:-13px auto 0;background:var(--panel);text-align:center;color:#ddd;padding:16px 12px 12px;position:relative}
.other-info h5{font-family:var(--head);font-weight:700;font-size:14px;color:var(--white)}
.other-info p{font-size:10.5px;line-height:14px;margin-top:6px}
.other-info span{display:block;font-size:10px;margin-top:1px}

/* newsletter */
.news-bg{left:0;top:2630px;width:1200px;height:414px;background:linear-gradient(#ffffff,#e7e7e7)}
.news-copy{left:0;top:2835px;width:1200px;text-align:center;font-size:16.5px;color:#555}
.news-form{left:273px;top:2880px;width:641px;height:64px;background:var(--white);border:1px solid #dcdcdc;box-shadow:0 1px 4px rgba(0,0,0,.08)}
.news-label{left:24px;top:24px;font-size:14px;color:#333}
.news-submit{left:482px;top:11px;width:145px;height:38px;background:var(--red);color:var(--white);font-weight:700;font-size:15px;display:flex;align-items:center;justify-content:center}

/* footer */
.site-footer{left:0;top:3044px;width:1200px;height:388px;background:#1f1f1f;color:#cfcfcf}
.foot-col{top:65px}
.foot-col h6{font-family:var(--head);font-weight:600;font-size:17px;color:#e8e8e8;margin-bottom:12px}
.foot-col li{list-style:none;font-size:14px;line-height:26.6px}
.contact-row{display:flex;gap:12px;font-size:14px;line-height:17px;margin-bottom:15px}
.social li{display:flex;align-items:center;gap:10px;line-height:34px}
.social i{width:26px;height:26px;border-radius:50%;background:var(--white);display:block}
.foot-rule{left:0;top:310px;width:1200px;height:1px;background:#333}
.copyright{left:0;top:334px;width:1200px;text-align:center;font-size:14px;color:#aaa}
</style>
</head>
<body>

<header class="site-header abs">
  <div class="brand abs"><span class="brand-mark"></span>K7M9</div>
  <nav class="main-nav abs">
    <span class="active">MARIN</span><span>SCREW</span><span>STICKS</span><span>NUTS</span><span>TRAYS</span><span>SCREW PIN</span><span>ABOUT US</span><span>CONTACT</span>
  </nav>
  <div class="login-btn abs">LOGIN</div>
  <svg class="cart abs" width="24" height="22" viewBox="0 0 24 22" fill="none" stroke="#bbb" stroke-width="1.6"><path d="M1 2h4l3 12h12l2-8H6"/><circle cx="9" cy="18" r="1.6"/><circle cx="19" cy="18" r="1.6"/></svg>
  <div class="cart-count abs">0</div>
</header>

<section class="hero">
  <div class="hero-visual abs" role="img" aria-label="Industrial ladder scene in grey and red with three blind rivets"></div>
  <div class="hero-kicker abs">WELCOME TO K7M9</div>
  <h1 class="hero-title abs">BLINDRIVET NUTS &amp;<br><span class="dim">ACCESSORIES</span></h1>
  <p class="hero-copy abs">Lorem ipsum dolor sit amet consectetuer adipiscing elit<br>Nam cursus Morbi ut mi Nullam enim leo egestas</p>
  <div class="hero-btn btn-outline abs">VIEW PRODUCT</div>
  <svg class="hero-arrow abs" style="left:55px" width="22" height="36" viewBox="0 0 22 36" fill="none" stroke="#fff" stroke-width="4"><path d="M18 3L4 18l14 15"/></svg>
  <svg class="hero-arrow abs" style="left:1121px" width="22" height="36" viewBox="0 0 22 36" fill="none" stroke="#fff" stroke-width="4"><path d="M4 3l14 15L4 33"/></svg>
</section>

<section class="categories">
  <div class="cat-card abs" style="left:109px;top:802px;width:319px;height:303px;padding-top:55px">
    <div class="cat-img" role="img" aria-label="Blind rivet product photo"></div>
    <h3>BLIND RIVETS</h3>
    <p>Augiat in pede Fusce tellus Sed metus augue convallis et vehicula ut pulvinar</p>
  </div>
  <div class="cat-card featured abs" style="left:428px;top:776px;width:343px;height:353px;padding-top:36px">
    <div class="cat-img" role="img" aria-label="Blind rivet nut product photo"></div>
    <h3>BLIND RIVET NUT</h3>
    <p>Augiat in pede Fusce tellus Sed metus augue convallis et vehicula ut pulvinar</p>
    <div class="cat-down"><svg width="16" height="10" viewBox="0 0 16 10" fill="none" stroke="#fff" stroke-width="2"><path d="M2 2l6 6 6-6"/></svg></div>
  </div>
  <div class="cat-card abs" style="left:771px;top:806px;width:317px;height:302px;padding-top:32px">
    <div class="cat-img" role="img" aria-label="Cordless riveting tool product photo" style="height:145px"></div>
    <h3>RIVETING TOOLS</h3>
    <p>Augiat in pede Fusce tellus Sed metus augue convallis et vehicula ut pulvinar</p>
  </div>
</section>

<section class="about">
  <svg class="about-band abs" width="1200" height="520" viewBox="0 0 1200 520">
    <defs><linearGradient id="aboutGrad" x1="0" x2="1" y1="0" y2="0"><stop offset="0" stop-color="#262626"/><stop offset=".45" stop-color="#3a2a2a"/><stop offset="1" stop-color="#c4161c"/></linearGradient></defs>
    <polygon points="0,71 602,0 1200,78 1200,444 602,519 0,441" fill="url(#aboutGrad)"/>
  </svg>
  <div class="about-img abs" role="img" aria-label="Stainless steel bolts and hex nuts"></div>
  <h2 class="about-title abs">ABOUT K7M9</h2>
  <div class="heading-rule abs" style="left:605px;top:1344px;width:169px;color:#fff"></div>
  <div class="about-copy abs">
    <p>K7M9 sells stainless steel fasteners to stores, retailers and industry. On our site you can find most known DIN and ISO standards in mounting. We also have a large range of Marine products in stainless steel. Welcome to look around our store.</p>
    <p>You navigate through the menu at the top of the page, if you want to see an overview of all products in a certain category</p>
  </div>
  <div class="about-btn btn-outline abs">LEARN MORE</div>
</section>

<section class="latest">
  <h2 class="sec-title abs" style="top:1747px">LATEST PRODUCTS</h2>
  <div class="heading-rule abs" style="left:521px;top:1795px;width:168px;color:#555"></div>
  <svg class="abs" style="left:86px;top:1956px" width="22" height="36" viewBox="0 0 22 36" fill="none" stroke="#999" stroke-width="3"><path d="M18 3L4 18l14 15"/></svg>
  <svg class="abs" style="left:1110px;top:1956px" width="22" height="36" viewBox="0 0 22 36" fill="none" stroke="#999" stroke-width="3"><path d="M4 3l14 15L4 33"/></svg>
  <div class="divider abs" style="left:362px"></div>
  <div class="divider abs" style="left:613px"></div>
  <div class="divider abs" style="left:872px"></div>
  <div class="product abs" style="left:117px;top:1855px">
    <div class="product-img" role="img" aria-label="Flat washer"></div>
    <h4>PRODUCT TITLE</h4><p>Donec convallis pede venenatis nibh<br>Duis quam Nam eget lacus</p><span class="btn-red">VIEW DETAIL</span>
  </div>
  <div class="product abs" style="left:365px;top:1855px">
    <div class="product-img" role="img" aria-label="Threaded insert"></div>
    <h4>PRODUCT TITLE</h4><p>Donec convallis pede venenatis nibh<br>Duis quam Nam eget lacus</p><span class="btn-red">VIEW DETAIL</span>
  </div>
  <div class="product abs" style="left:617px;top:1855px">
    <div class="product-img" role="img" aria-label="Round head pin"></div>
    <h4>PRODUCT TITLE</h4><p>Donec convallis pede venenatis nibh<br>Duis quam Nam eget lacus</p><span class="btn-red">VIEW DETAIL</span>
  </div>
  <div class="product abs" style="left:874px;top:1855px">
    <div class="product-img" role="img" aria-label="Hex nut"></div>
    <h4>PRODUCT TITLE</h4><p>Donec convallis pede venenatis nibh<br>Duis quam Nam eget lacus</p><span class="btn-red">VIEW DETAIL</span>
  </div>
</section>

<section class="other">
  <div class="news-bg abs"></div>
  <svg class="other-band abs" width="1200" height="490" viewBox="0 0 1200 490">
    <polygon points="0,0 1200,0 1200,432 602,489 0,432" fill="#1c1c1c"/>
  </svg>
  <h2 class="sec-title abs" style="top:2258px;color:#e8e8e8">OTEHR PRODUCTS</h2>
  <div class="heading-rule abs" style="left:506px;top:2305px;width:168px;color:#ddd"></div>
  <svg class="abs" style="left:105px;top:2441px" width="22" height="36" viewBox="0 0 22 36" fill="none" stroke="#fff" stroke-width="3"><path d="M18 3L4 18l14 15"/></svg>
  <svg class="abs" style="left:1076px;top:2441px" width="22" height="36" viewBox="0 0 22 36" fill="none" stroke="#fff" stroke-width="3"><path d="M4 3l14 15L4 33"/></svg>
  <div class="other-card abs" style="left:151px;top:2353px">
    <div class="other-img" role="img" aria-label="Gloved hand using a power drill" style="background:linear-gradient(135deg,#1e6a7a,#1a3a1a 60%,#3a7a30)"></div>
    <div class="other-info"><h5>PRODUCT TITLE</h5><p>Donec convallis pede venenatis nibh Duis quam Nam eget lacus</p><span>READ MORE</span></div>
  </div>
  <div class="other-card abs" style="left:382px;top:2353px">
    <div class="other-img" role="img" aria-label="Close-up of blue steel nuts and bolts" style="background:linear-gradient(135deg,#5a6a8a,#1e2a40)"></div>
    <div class="other-info"><h5>PRODUCT TITLE</h5><p>Donec convallis pede venenatis nibh Duis quam Nam eget lacus</p><span>READ MORE</span></div>
  </div>
  <div class="other-card abs" style="left:611px;top:2353px">
    <div class="other-img" role="img" aria-label="Pile of steel screws" style="background:linear-gradient(135deg,#d8d8d8,#8a8a8a)"></div>
    <div class="other-info"><h5>PRODUCT TITLE</h5><p>Donec convallis pede venenatis nibh Duis quam Nam eget lacus</p><span>READ MORE</span></div>
  </div>
  <div class="other-card abs" style="left:842px;top:2353px">
    <div class="other-img" role="img" aria-label="Assorted hex nuts and bolts" style="background:linear-gradient(135deg,#a89a7a,#5a5040)"></div>
    <div class="other-info"><h5>PRODUCT TITLE</h5><p>Donec convallis pede venenatis nibh Duis quam Nam eget lacus</p><span>READ MORE</span></div>
  </div>
</section>

<section class="newsletter">
  <h2 class="sec-title abs" style="top:2765px;font-size:30px">SIGN UP OUR NEWSLETTERS</h2>
  <div class="heading-rule abs" style="left:501px;top:2811px;width:168px;color:#555"></div>
  <p class="news-copy abs">Lorem ipsum dolor sit amet consectetuer adipiscing elit Nam cursus Morbi ut</p>
  <div class="news-form abs">
    <span class="news-label abs">EMAIL ADDRESS</span>
    <span class="news-submit abs">SUBSCRIBE</span>
  </div>
</section>

<footer class="site-footer abs">
  <div class="foot-col abs" style="left:145px">
    <h6 style="margin-bottom:22px">CONTACT US</h6>
    <div class="contact-row"><svg width="16" height="18" viewBox="0 0 16 18" fill="none" stroke="#ccc" stroke-width="1.4"><path d="M8 17s6-6 6-10A6 6 0 002 7c0 4 6 10 6 10z"/><circle cx="8" cy="7" r="2"/></svg><span>48 Harbor Lane #3<br>Dalton 20417 DL</span></div>
    <div class="contact-row"><svg width="16" height="16" viewBox="0 0 16 16" fill="none" stroke="#ccc" stroke-width="1.4"><path d="M3 1h3l1.5 4-2 1.5a9 9 0 004 4L11 8.5l4 1.5v3a2 2 0 01-2 2A13 13 0 011 3a2 2 0 012-2z"/></svg><span>555.014.2871</span></div>
    <div class="contact-row"><svg width="16" height="14" viewBox="0 0 16 14" fill="none" stroke="#ccc" stroke-width="1.4"><rect x="1" y="2" width="14" height="10"/><path d="M1 2l7 6 7-6"/></svg><span>hello@k7m9.se</span></div>
  </div>
  <div class="foot-col abs" style="left:436px">
    <h6>COMPANY</h6>
    <ul><li>Home</li><li>About us</li><li>Services</li><li>Why Us</li><li>Contact</li></ul>
  </div>
  <div class="foot-col abs" style="left:617px">
    <h6>RESOURCES</h6>
    <ul><li>Resources</li><li>Projects</li><li>Gallery</li><li>News</li><li>Sitemap</li></ul>
  </div>
  <div class="foot-col abs" style="left:842px">
    <h6 style="margin-bottom:4px">GET IN TOUCH</h6>
    <ul class="social"><li><i></i>Chirper</li><li><i></i>Friendbook</li><li><i></i>WorkLink</li><li><i></i>Snapgram</li></ul>
  </div>
  <div class="foot-rule abs"></div>
  <p class="copyright abs">Copyright © 2019 All right reserved</p>
</footer>

</body>
</html>
```